Wine Label for a White and a Red Wine from Italy

We have a very good idea of what we want with artwork. We need you to please design a 'template' with the text so we can change out the artwork from year to year. Samples are shown of what we are looking for. We are looking for options with the two basic designs. Brand name of wine is: Valora di Castegno. Both wines are in a light green Bordeaux-style bottle (note: we don't show a light green bottle in the mockup but please remember the bottle is light green). Artwork is provided. We'd like to see either the green or blue butterfly on the white wine, the red butterfly is for the red wine. Please base the design on the attached label from Brailey and/or the attached label from Chateau Mervanges.

Target Market(s)

Millennials, women

Requirements
Must have
• The artwork (butterflies) attached.
Nice to have
• Elegant, readable fonts. Please make the text so it can be changed by the printer. Please make it so the artwork can be changed too.

```html
<!DOCTYPE html>
<html lang="en">
<head>
<meta charset="utf-8">
<title>Valora di Castegno – Barrel Select Labels</title>
<link rel="stylesheet" href="https://fonts.googleapis.com/css2?family=Cinzel:wght@400;500&family=Cormorant+Garamond:wght@400;500&display=swap">
<style>
  :root {
    --page-bg: #ffffff;
    --label-bg: #ffffff;
    --label-edge: #c9c9c9;
    --ink: #1c1c1c;
    --ink-soft: #6d6d6d;
    --bianco-deep: #4f6b3a;
    --bianco-mid: #9fbf7e;
    --bianco-pale: #e3ecd6;
    --rosso-deep: #b3261e;
    --rosso-mid: #e0541f;
    --rosso-amber: #f2b43a;
  }
  * { margin: 0; padding: 0; box-sizing: border-box; }
  html, body {
    width: 1200px;
    height: 764px;
    overflow: hidden;
    background: var(--page-bg);
  }
  .label-set {
    position: relative;
    width: 1200px;
    height: 764px;
    display: flex;
    justify-content: center;
    align-items: center;
    gap: 60px;
  }
  .label {
    position: relative;
    width: 364px;
    height: 560px;
    background: var(--label-bg);
    border: 1px solid var(--label-edge);
    color: var(--ink);
    text-align: center;
  }
  .label > * {
    position: absolute;
    left: 0;
    right: 0;
  }
  .brand-name {
    top: 46px;
    font-family: "Cinzel", serif;
    font-weight: 400;
    font-size: 37px;
    letter-spacing: 0.14em;
    line-height: 1;
  }
  .brand-region {
    top: 91px;
    font-family: "Cormorant Garamond", serif;
    font-weight: 500;
    font-size: 15px;
    letter-spacing: 0.16em;
    line-height: 1;
  }
  .cuvee {
    top: 131px;
    font-family: "Cormorant Garamond", serif;
    font-size: 12.5px;
    letter-spacing: 0.28em;
    color: var(--ink-soft);
    line-height: 1;
  }
  .artwork {
    top: 170px;
    left: 50%;
    right: auto;
    width: 220px;
    height: 190px;
    transform: translateX(-50%);
  }
  .artwork--bianco {
    background: radial-gradient(ellipse at 52% 48%, var(--bianco-deep) 0%, var(--bianco-mid) 30%, var(--bianco-pale) 58%, rgba(255,255,255,0) 74%);
  }
  .artwork--rosso {
    background: radial-gradient(ellipse at 50% 50%, var(--rosso-deep) 0%, var(--rosso-mid) 32%, var(--rosso-amber) 55%, rgba(255,255,255,0) 74%);
  }
  .vintage {
    top: 381px;
    font-family: "Cormorant Garamond", serif;
    font-size: 23px;
    letter-spacing: 0.04em;
    line-height: 1;
  }
  .varietal {
    top: 407px;
    font-family: "Cormorant Garamond", serif;
    font-size: 23px;
    letter-spacing: 0.08em;
    line-height: 1;
  }
  .origin {
    top: 446px;
    font-family: "Cormorant Garamond", serif;
    font-size: 12.5px;
    letter-spacing: 0.28em;
    color: var(--ink-soft);
    line-height: 1;
  }
  .producer {
    top: 486px;
    font-family: "Cinzel", serif;
    font-size: 11px;
    letter-spacing: 0.04em;
    line-height: 1;
  }
  .farming {
    top: 505px;
    font-family: "Cinzel", serif;
    font-size: 9.5px;
    letter-spacing: 0.05em;
    line-height: 1;
    text-transform: lowercase;
    font-variant: small-caps;
  }
</style>
</head>
<body>
  <main class="label-set">
    <article class="label label--bianco">
      <h1 class="brand-name">VALORA</h1>
      <p class="brand-region">DI CASTEGNO</p>
      <p class="cuvee">BARREL SELECT</p>
      <div class="artwork artwork--bianco" role="img" aria-label="Watercolour green butterfly artwork, replaceable each vintage"></div>
      <p class="vintage">2018</p>
      <p class="varietal">BIANCO</p>
      <p class="origin">PIEMONTE, ITALY</p>
      <p class="producer">Artisanally Crafted by Cantina Due Colli</p>
      <p class="farming">Sustainably Farmed</p>
    </article>

    <article class="label label--rosso">
      <h1 class="brand-name">VALORA</h1>
      <p class="brand-region">DI CASTEGNO</p>
      <p class="cuvee">BARREL SELECT</p>
      <div class="artwork artwork--rosso" role="img" aria-label="Watercolour red butterfly on amber wash artwork, replaceable each vintage"></div>
      <p class="vintage">2018</p>
      <p class="varietal">ROSSO</p>
      <p class="origin">PIEMONTE, ITALY</p>
      <p class="producer">Artisanally Crafted by Cantina Due Colli</p>
      <p class="farming">Sustainably Farmed</p>
    </article>
  </main>
</body>
</html>
```